Fancy flyer to entice High School Students

http://quillmarsh.com needs a marketing slick/flyer to pass out. The marketing text is below(feel free to place where you think appropriate).

* 8th grade to 12th grade (or 8th graders to 12th graders)
* Land a real job internship(instead of Grubbins)
* 100's of internships available
* Learn how to start your own business out of High School making way more than minimum wage
* In college when interviewing for an internship don't be the guy that answers "no, sorry, this would be my first internship" putting you at a huge disadvantage"
* Fill in the Contact Us form at http://quillmarsh.com at the bottom left corner to find out more information

We will be evaluating design with this blog post in mind....
http://trovelinkdigest.com/color-influence-buyers/

We like attention grabbing contact us type stuff and calls to action. If you feel it is appropriate to change the marketing text to make your flyer stand out, please feel free. I am not the best at marketing and am the first to admit it.
Updates

A simple 8.5 x 11 flyer would be great.

Target Market(s)

High School students, male and female with high grade point averages(smart students). For the top 20% of their class.

Industry/Entity Type

Marketing

Requirements
Must have
• good call to action

```html
<!DOCTYPE html>
<html lang="en">
<head>
<meta charset="utf-8">
<title>Quillmarsh Software – Real Internships Flyer</title>
<link href="https://fonts.googleapis.com/css2?family=PT+Sans+Narrow:wght@700&family=Open+Sans:wght@400;600&display=swap" rel="stylesheet">
<style>
  :root {
    --ink: #333333;
    --navy: #2a2f8a;
    --pink: #d81b6a;
    --magenta: #e0468f;
    --amber: #c9791e;
    --green: #3ab54a;
    --purple: #6a3d9a;
    --cream: #fbf1dc;
    --gold: #f0bb62;
    --footer: #3a3a3a;
    --label: #f29a1f;
    --white: #ffffff;
  }
  * { margin: 0; padding: 0; box-sizing: border-box; }
  html, body { width: 931px; height: 1200px; overflow: hidden; background: #eeeeee; }
  .flyer {
    position: relative; width: 931px; height: 1200px; overflow: hidden;
    background: linear-gradient(180deg, var(--cream) 45%, #f8dca4 80%, var(--gold) 100%);
    font-family: "Open Sans", sans-serif;
  }
  .hero-photo {
    position: absolute; left: 0; top: 0; width: 931px; height: 560px;
    background: linear-gradient(120deg, #3e5f9e 0%, #8a9cc4 35%, #d9c2b0 60%, #6b4d8a 100%);
  }
  .waves { position: absolute; left: 0; top: 0; width: 931px; height: 1200px; }
  .brand {
    position: absolute; left: 564px; top: 42px; width: 321px; height: 55px;
    background: var(--white); display: flex; align-items: center; justify-content: center; gap: 10px;
    font-family: "Open Sans", sans-serif; font-weight: 600; font-size: 26px; color: var(--ink);
  }
  .brand-mark { width: 18px; height: 18px; background: var(--ink); }
  .headline {
    position: absolute; left: 304px; top: 560px;
    font-family: "PT Sans Narrow", sans-serif; font-weight: 700; font-size: 58px; line-height: 1.0;
    color: var(--ink); text-transform: uppercase;
  }
  .contact-line {
    position: absolute; left: 304px; top: 700px;
    font-family: "PT Sans Narrow", sans-serif; font-weight: 700; color: var(--navy); font-size: 36px;
  }
  .contact-line .phone { color: var(--ink); font-size: 42px; margin-left: 10px; }
  .student-photo {
    position: absolute; left: 29px; top: 615px; width: 250px; height: 500px;
    background: linear-gradient(180deg, #c99b7e 0%, #f2d3d8 35%, #e6a0b5 55%, #8aa6c9 100%);
    border-radius: 120px 120px 0 0;
  }
  .benefits { position: absolute; left: 290px; top: 788px; width: 641px; list-style: none; }
  .benefits li {
    color: var(--white); font-size: 19px; line-height: 26px; padding: 4px 14px 4px 16px;
    margin-bottom: 8px; border-radius: 6px 0 0 6px;
    clip-path: polygon(0 0, 100% 0, 97% 100%, 0 100%);
  }
  .benefits .grade { background: var(--pink); }
  .benefits .job { background: var(--amber); }
  .benefits .count { background: var(--green); }
  .benefits .business { background: var(--magenta); }
  .benefits .college { background: var(--purple); }
  .footer {
    position: absolute; left: 0; top: 1120px; width: 931px; height: 80px;
    background: var(--footer); color: var(--white); font-size: 19px;
    border-top: 3px solid #bfbfbf;
  }
  .footer .item { position: absolute; top: 14px; line-height: 25px; }
  .footer .label { color: var(--label); font-weight: 600; }
  .footer .email { left: 54px; }
  .footer .web { left: 306px; }
  .footer .address { left: 588px; }
</style>
</head>
<body>
<div class="flyer">
  <div class="hero-photo" role="img" aria-label="Photo of smiling high school students with books in a school hallway by lockers"></div>

  <svg class="waves" viewBox="0 0 931 1200" aria-hidden="true">
    <path d="M0,565 C250,490 560,610 931,520 L931,1200 L0,1200 Z" fill="var(--cream)"/>
    <path d="M0,520 C250,465 560,585 931,495 L931,530 C560,612 250,495 0,568 Z" fill="var(--ink)"/>
    <path d="M0,478 C200,430 480,470 700,520 C460,478 220,470 0,525 Z" fill="var(--pink)"/>
    <path d="M380,540 C600,585 780,530 931,480 L931,500 C780,555 600,600 380,548 Z" fill="var(--green)"/>
  </svg>

  <div class="brand"><span class="brand-mark"></span>Quillmarsh Software</div>

  <h1 class="headline">We provide<br>real intership!</h1>
  <p class="contact-line">Contact us today <span class="phone">(555) 014-2287</span></p>

  <div class="student-photo" role="img" aria-label="Photo of a smiling student with a backpack holding a notebook"></div>

  <ul class="benefits">
    <li class="grade">8th graders to 12th graders)</li>
    <li class="job">Land a real job internship (instead of Grubbins)</li>
    <li class="count">100's of internships available</li>
    <li class="business">Learn how to start your own business out of High School making way more than minimum wage</li>
    <li class="college">In college when interviewing for an internship don't be the guy that answers "no, sorry, this would be my first internship" putting you at a huge disadvantage"</li>
  </ul>

  <footer class="footer">
    <div class="item email"><div class="label">Email</div>info@quillmarsh.com</div>
    <div class="item web"><div class="label">Web</div>www.quillmarsh.com</div>
    <div class="item address"><span class="label">Add</span> : 4418 Larkspur Ave.<br>#212, Fernvale, CO 80000</div>
  </footer>
</div>
</body>
</html>
```